Motor Vault Website - Part of the Brantley Group

A complimentary website is required for the launch of a 'Motor Vault' - a new service launched by industry renowned BRANTLEY. Motor Vault is an industry-first brand that designs and builds unique subterranean car parks for private residential homes in London and the influential counties within the UK. Please see here the direction of a new BRANTLEY Website - we would like Motor Vault to be complimentary and sit alongside BRANTLEY harmoniously - https://www.brantleyhomes.example/brantley-nu-staging Brantley have some images, but whilst more professional images are in production - we have also attached pixmora photos- named clearly as pixmora. **Attached files include JPEG, .eps of logo and Brantley library images and Pixmora Library Images - two versions of logo dependent on background colour. - Website needs to be sleek, chic and masculine.- Colour Palette - Grey/ Black/ White - Same visiual journey as Brantley website- Required areas within the sit include - About Us / Our Work / Contact Page

Target Market(s)

Luxury
Men

Number of Pages Required

2 page

Font styles to use
Sans Serif

Colors
e8e8e8
757575
1b1b1b
000000
9d9d9d
cbcbcb
f5f5f5

Requirements
Must have
• Complimentary of this site - https://www.brantleyhomes.example/brantley-nu-staging
Should not have
• Colour

```html
<!DOCTYPE html>
<html lang="en">
<head>
<meta charset="utf-8">
<title>Motor Vault — Part of the Brantley Group</title>
<link rel="stylesheet" href="https://fonts.googleapis.com/css2?family=Libre+Baskerville:ital,wght@0,400;0,700;1,400&display=swap">
<style>
  :root {
    --black: #000000;
    --ink: #1b1b1b;
    --grey-dark: #757575;
    --grey: #9d9d9d;
    --grey-light: #cbcbcb;
    --mist: #e8e8e8;
    --paper: #f5f5f5;
    --white: #ffffff;
    --serif: 'Libre Baskerville', Georgia, serif;
  }
  * { box-sizing: border-box; margin: 0; padding: 0; }
  html, body { width: 1200px; height: 2544px; overflow: hidden; background: var(--white); }
  body { position: relative; font-family: var(--serif); color: var(--ink); }
  .abs { position: absolute; }

  /* Hero */
  .hero { left: 0; top: 0; width: 1200px; height: 615px;
    background: radial-gradient(ellipse at 50% 70%, #3a3a3a 0%, #161616 45%, #050505 100%); }
  .hero-brand { left: 0; top: 262px; width: 1200px; text-align: center; color: var(--white); }
  .brand-row { display: inline-flex; align-items: center; gap: 18px; }
  .brand-mark { width: 48px; height: 48px; background: var(--white); }
  .brand-name { font-weight: 700; font-size: 58px; letter-spacing: 2px; line-height: 1; }
  .hero-tag { display: block; margin: 6px 0 0 300px; font-size: 11px; letter-spacing: 2px; color: var(--grey); }
  .hero-arrow { left: 592px; top: 566px; }

  /* Intro */
  .intro { left: 160px; top: 692px; width: 700px; font-size: 26px; line-height: 47px; color: var(--ink); }
  .intro-rule { left: 675px; top: 890px; width: 130px; height: 1px; background: var(--grey-light); }
  .btn-dark { left: 836px; top: 867px; width: 202px; height: 45px; background: var(--black); color: var(--white);
    font-size: 13px; display: flex; align-items: center; justify-content: center; }

  /* Featured */
  .featured { left: 0; top: 1010px; width: 1200px; height: 735px;
    background: linear-gradient(180deg, #050505, #000 60%, #0c0c0c); }
  .feature-photo { left: 0; top: 890px; width: 583px; height: 238px;
    background: linear-gradient(135deg, #4a4a4a, #1e1e1e 55%, #6a6a6a); }
  .featured-title { left: 632px; top: 1120px; font-size: 27px; line-height: 38px; color: var(--white); }

  .project { width: 406px; height: 286px; overflow: hidden; }
  .project-photo { width: 100%; height: 100%; background: linear-gradient(160deg, #7a7a7a, #2c2c2c 55%, #101010); }
  .project-photo.alt { background: linear-gradient(200deg, #8a8a8a, #3a3a3a 50%, #111); }
  .project-name { position: absolute; left: 24px; bottom: 42px; font-size: 21px; color: var(--white); }
  .project-meta { position: absolute; left: 24px; bottom: 20px; font-size: 13px; color: var(--grey); }
  .project-go { position: absolute; right: 0; bottom: 0; width: 45px; height: 36px; background: var(--white);
    display: flex; align-items: center; justify-content: center; }
  .project-go.ghost { background: transparent; }

  .btn-outline { left: 498px; top: 1918px; width: 202px; height: 44px; border: 1.5px solid var(--ink);
    font-size: 13px; display: flex; align-items: center; justify-content: center; }

  /* Newsletter */
  .newsletter { left: 0; top: 2020px; width: 1200px; height: 195px; background: var(--black); }
  .newsletter-title { left: 160px; top: 2080px; font-size: 24px; line-height: 38px; font-weight: 700; color: var(--white); }
  .field { top: 2108px; width: 148px; height: 27px; border-bottom: 1px solid var(--grey-dark);
    font-size: 12px; color: var(--grey-dark); }
  .btn-light { left: 933px; top: 2098px; width: 105px; height: 37px; background: var(--white); color: var(--ink);
    font-size: 13px; display: flex; align-items: center; justify-content: center; }

  /* Footer */
  .footer-brand { left: 160px; top: 2287px; color: var(--ink); }
  .footer-brand .brand-mark { width: 26px; height: 26px; background: var(--ink); }
  .footer-brand .brand-row { gap: 9px; }
  .footer-brand .brand-name { font-size: 30px; letter-spacing: 1px; }
  .footer-brand .hero-tag { margin: 3px 0 0 38px; font-size: 7px; letter-spacing: 1px; }
  .col-head { top: 2290px; font-size: 13px; letter-spacing: 1.5px; color: var(--grey); }
  .col-list { top: 2326px; list-style: none; font-size: 13px; line-height: 32px; color: var(--ink); }
  .social { left: 862px; top: 2330px; display: flex; gap: 13px; }
  .social span { width: 34px; height: 34px; display: block; }
  .legal { top: 2502px; font-size: 12px; color: var(--grey); }
</style>
</head>
<body>

<header class="abs hero" role="img" aria-label="Dark black and white photograph of a long underground parking corridor with light stripes on the floor"></header>
<div class="abs hero-brand">
  <div class="brand-row"><span class="brand-mark"></span><span class="brand-name">MOTOR VAULT</span></div>
  <span class="hero-tag">PART OF THE BRANTLEY GROUP</span>
</div>
<svg class="abs hero-arrow" width="16" height="20" viewBox="0 0 16 20"><path d="M8 2v15M3 12l5 5 5-5" stroke="#fff" stroke-width="1.6" fill="none"/></svg>

<p class="abs intro">Designs and builds <em>unique</em> subterranean car parks for private residential homes in <em>London</em> and the influential counties within the UK.</p>
<span class="abs intro-rule"></span>
<a class="abs btn-dark">Find out more</a>

<section class="abs featured"></section>
<div class="abs feature-photo" role="img" aria-label="Black and white photograph of a welder working on steel beams on a construction site"></div>
<h2 class="abs featured-title" style="font-weight:400">See our latest<br>featured projects</h2>

<article class="abs project" style="left:160px;top:1250px">
  <div class="project-photo" role="img" aria-label="Black and white photograph of an underground car park construction with light beams"></div>
  <h3 class="project-name" style="font-weight:400">Ashcombe Car Park</h3><span class="project-meta">London, 2018</span>
  <span class="project-go"><svg width="10" height="12" viewBox="0 0 10 12"><path d="M3 2l4 4-4 4" stroke="#1b1b1b" stroke-width="1.6" fill="none"/></svg></span>
</article>
<article class="abs project" style="left:633px;top:1250px">
  <div class="project-photo alt" role="img" aria-label="Black and white photograph of an excavation site with a digger under steel props"></div>
  <h3 class="project-name" style="font-weight:400">Ashcombe Car Park</h3><span class="project-meta">London, 2018</span>
  <span class="project-go"><svg width="10" height="12" viewBox="0 0 10 12"><path d="M3 2l4 4-4 4" stroke="#1b1b1b" stroke-width="1.6" fill="none"/></svg></span>
</article>
<article class="abs project" style="left:160px;top:1580px">
  <div class="project-photo" role="img" aria-label="Black and white photograph of a steel roof framework seen from below"></div>
  <h3 class="project-name" style="font-weight:400">Ashcombe Car Park</h3><span class="project-meta">London, 2018</span>
  <span class="project-go"><svg width="10" height="12" viewBox="0 0 10 12"><path d="M3 2l4 4-4 4" stroke="#1b1b1b" stroke-width="1.6" fill="none"/></svg></span>
</article>
<article class="abs project" style="left:633px;top:1580px">
  <div class="project-photo alt" role="img" aria-label="Black and white photograph of an excavation site with a digger under steel props"></div>
  <h3 class="project-name" style="font-weight:400">Ashcombe Car Park</h3><span class="project-meta">London, 2018</span>
  <span class="project-go ghost"><svg width="10" height="12" viewBox="0 0 10 12"><path d="M3 2l4 4-4 4" stroke="#fff" stroke-width="1.6" fill="none"/></svg></span>
</article>

<a class="abs btn-outline">View more projects</a>

<section class="abs newsletter"></section>
<h2 class="abs newsletter-title">Stay up to date with our news<br>and projects</h2>
<span class="abs field" style="left:588px">Full name</span>
<span class="abs field" style="left:755px">Email</span>
<a class="abs btn-light">Subscribe</a>

<div class="abs footer-brand">
  <div class="brand-row"><span class="brand-mark"></span><span class="brand-name">MOTOR VAULT</span></div>
  <span class="hero-tag">PART OF THE BRANTLEY GROUP</span>
</div>

<h4 class="abs col-head" style="left:512px;font-weight:400">COMPANY</h4>
<ul class="abs col-list" style="left:512px"><li>Home</li><li>About</li><li>Our work</li><li>Contact</li></ul>

<h4 class="abs col-head" style="left:685px;font-weight:400">CONTACT</h4>
<ul class="abs col-list" style="left:685px"><li style="line-height:26px">27 Harlow Mews,<br>London, W2 9QT</li><li style="margin-top:14px">Tel: 0207 555 0148</li></ul>

<h4 class="abs col-head" style="left:862px;font-weight:400">FOLLOW US</h4>
<div class="abs social">
  <span><svg width="34" height="34" viewBox="0 0 34 34"><path d="M17 0L34 17 17 34 0 17Z" fill="#000"/></svg></span>
  <span><svg width="34" height="34" viewBox="0 0 34 34"><path d="M17 0L34 17 17 34 0 17Z" fill="#000"/></svg></span>
  <span><svg width="34" height="34" viewBox="0 0 34 34"><path d="M17 0L34 17 17 34 0 17Z" fill="#000"/></svg></span>
  <span><svg width="34" height="34" viewBox="0 0 34 34"><path d="M17 0L34 17 17 34 0 17Z" fill="#000"/></svg></span>
</div>

<span class="abs legal" style="left:160px">Copyright© Motor Vault 2019</span>
<span class="abs legal" style="left:776px">Terms and Conditions</span>
<span class="abs legal" style="left:950px">Privacy Policy</span>

</body>
</html>
```